Quillby Housecrafters Door Hanger design, Postcard and presentation folders Design

we are a home improvement company in Portland Oregon, are main service is roofing but we also do gutters, painting and pressure washing. we are a certified roofing contractor for TRV. We have over 20years of experince in the roofing industry we use top quality materials. Our mission is to do quality work and provide the best service.
Updates

This door hangers are going to be share to homeowners where we are currently working at! I will like to have a square maybe 2 inch wide and 1 inch hide (blank) for me to put the address where we are working at. So we want to give a direct message to homeowners who we are and why we are there for. Our services are roofing, gutters, painting, and pressure washing. But 95% of the door hangers should give the message that we are a roofing contractor. We are also certified by TRV which means all of our new roof projects have a 50 year warranty which only 2% of roofing contractor can offer that. We also offer finance, and all quality work. I will like to add photos of our trucks since all of them are wrap which will build them trust.

Target Market(s)

This door hangers should be custom for Homeowners with residential Homes,,, Average customer are between 40 & 65 Years old.

Industry/Entity Type

Roofing

Contact Information for Business Card

Logo, name, phone number, credentials, and services like roofing gutters painting and pressure washing

Font styles to use
Serif
Sans Serif
Decorative

Colors
33b8a4
5c5c5c

Requirements
Must have
• I want tho have a folder design just like this business card sample i uploaded. Teal and charcoal with services ...
Nice to have
• company trucks, job photo, crew photo and credential photos
Should not have
• I dont want it too busy or crowded..

```html
<!DOCTYPE html>
<html lang="en">
<head>
<meta charset="utf-8">
<title>Quillby Housecrafters Door Hanger</title>
<link rel="stylesheet" href="https://fonts.googleapis.com/css2?family=Roboto:wght@400;500;700;900&family=Roboto+Condensed:wght@500;700&display=swap">
<style>
:root{
  --teal:#1e9585;
  --teal-dark:#17796c;
  --charcoal:#5c5c5c;
  --charcoal-dark:#4a4a4a;
  --light-grey:#b9b9b9;
  --red:#d2262b;
  --white:#ffffff;
  --page:#e4e4e4;
}
*{box-sizing:border-box;margin:0;padding:0}
html,body{width:1200px;height:1019px;overflow:hidden}
body{background:var(--page);position:relative;font-family:"Roboto",Arial,sans-serif}
.card{position:absolute;width:812px;background:var(--white);overflow:hidden;box-shadow:0 2px 6px rgba(0,0,0,.18)}
.card--front{left:141px;top:80px;height:405px}
.card--back{left:248px;top:534px;height:407px}
.abs{position:absolute}

/* front */
.front-band{left:0;top:0}
.brand{left:40px;top:160px;width:240px;text-align:center}
.brand__name{display:flex;align-items:center;gap:8px;justify-content:center;color:var(--teal);font-weight:700;font-size:21px;letter-spacing:.3px}
.brand__mark{width:14px;height:14px;background:var(--teal)}
.brand__tag{margin-top:6px;color:var(--charcoal);font-weight:500;font-size:13px;letter-spacing:1.2px}
.truck-photo{left:0;top:235px;width:300px;height:170px;background:linear-gradient(90deg,#8d9aa2 0%,#b6c0c4 45%,rgba(255,255,255,0) 100%)}
.headline{right:34px;top:20px;text-align:right;color:var(--white)}
.headline__lead{font-size:19px;font-weight:500;line-height:25px;letter-spacing:.3px}
.headline__phone{font-size:30px;font-weight:700;margin-top:7px;letter-spacing:.3px}
.cert-badge{left:334px;top:150px;width:172px;height:58px}
.cert-note{left:334px;top:212px;width:172px;text-align:center;color:var(--red);font-size:13px;font-weight:700}
.badge{top:165px}
.badge--round{left:524px;width:42px;height:42px;border-radius:50%;border:3px solid var(--light-grey);background:#eef0f0}
.badge--dark{left:579px;width:100px;height:40px;border-radius:7px;background:#1d1d1d;border:2px solid #999}
.badge--outline{left:692px;width:78px;height:40px;border-radius:7px;border:2px solid #333;background:var(--white)}
.finance{left:524px;top:214px;color:var(--light-grey);font-size:19px;font-weight:500;letter-spacing:.4px}
.notice{left:143px;top:251px;width:637px;height:126px;border-radius:14px;background:var(--charcoal);border:3px solid #8a8a8a;padding:10px 0 0 19px;color:var(--white)}
.notice__small{font-size:27px;font-weight:700;letter-spacing:.3px;line-height:30px}
.notice__big{font-size:46px;font-weight:900;letter-spacing:.5px;line-height:44px}
.address-line{left:13px;top:88px;width:598px;height:26px;border-radius:4px;background:linear-gradient(90deg,#f4f4f4,#d9d9d9)}

/* back */
.job-photo{width:122px;height:99px}
.job-photo--shingles{left:13px;top:13px;background:linear-gradient(135deg,#5c6a78,#2f3338)}
.job-photo--gutter{left:141px;top:13px;background:linear-gradient(160deg,#c9c9c9,#5b6470)}
.job-photo--painter{left:270px;top:13px;background:linear-gradient(160deg,#9c9d8a,#3a4250)}
.job-photo--siding{left:13px;top:118px;background:linear-gradient(180deg,#949984,#7c8270)}
.job-photo--washing{left:141px;top:118px;background:linear-gradient(160deg,#c4bcaa,#7d7a72)}
.job-photo--underlay{left:270px;top:118px;background:linear-gradient(160deg,#3f6aa8,#25467a)}
.fleet-photo{left:403px;top:13px;width:397px;height:205px;background:linear-gradient(180deg,#5b6b5a 0%,#c9d3d6 45%,#e8ecec 70%,#3b3f42 100%)}
.services{left:13px;top:226px;width:380px;height:166px;background:var(--teal)}
.services__title{position:absolute;left:12px;top:12px;width:354px;height:48px;background:var(--charcoal);color:var(--white);font-size:27px;font-weight:700;text-align:center;line-height:48px}
.services__list{position:absolute;left:23px;top:74px;list-style:none;display:grid;grid-template-columns:138px auto;row-gap:5px}
.services__item{display:flex;align-items:center;gap:9px;color:var(--white);font-family:"Roboto Condensed",Arial,sans-serif;font-weight:700;font-size:20px;line-height:21px;letter-spacing:.2px}
.services__icon{width:14px;height:14px;flex:none}
.sign-off{left:403px;top:250px;width:397px;text-align:center}
.sign-off__name{display:flex;align-items:center;justify-content:center;gap:8px;color:var(--teal);font-weight:700;font-size:22px}
.sign-off__mark{width:14px;height:14px;background:var(--teal)}
.sign-off__rule{margin:14px auto 8px;width:320px;height:3px;background:var(--teal)}
.sign-off__url{font-family:"Roboto Condensed",Arial,sans-serif;font-weight:700;font-size:28px;color:var(--charcoal);letter-spacing:.2px}
</style>
</head>
<body>

<section class="card card--front">
  <svg class="abs front-band" width="812" height="133" viewBox="0 0 812 133" aria-hidden="true">
    <polygon points="0,0 117,0 0,92" fill="var(--teal)"/>
    <polygon points="117,0 812,0 812,133 305,133" fill="var(--teal)"/>
  </svg>

  <div class="abs truck-photo" role="img" aria-label="Photo of a wrapped company pickup truck parked on a residential street"></div>

  <div class="abs brand">
    <div class="brand__name"><span class="brand__mark"></span>Quillby Housecrafters</div>
    <div class="brand__tag">WHEN QUALITY MATTERS</div>
  </div>

  <div class="abs headline">
    <p class="headline__lead">PORTLAND’S TOP-RATED ROOFING COMPANY.</p>
    <p class="headline__lead">Let Our Experts Help With Your Next Home Project.</p>
    <p class="headline__phone">TALK TO US: 503-555-0148</p>
  </div>

  <div class="abs cert-badge" role="img" aria-label="TRV certified Weather Guard roofing contractor badge">
    <svg width="172" height="58" viewBox="0 0 172 58" aria-hidden="true">
      <polygon points="20,14 86,0 152,14" fill="#9a9a9a"/>
      <rect x="0" y="14" width="172" height="42" fill="var(--red)"/>
    </svg>
  </div>
  <p class="abs cert-note">WITH 50 YEAR WARRANTY</p>

  <div class="abs badge badge--round" role="img" aria-label="Screened and approved listing badge"></div>
  <div class="abs badge badge--dark" role="img" aria-label="Accredited business badge"></div>
  <div class="abs badge badge--outline" role="img" aria-label="Review site badge"></div>
  <p class="abs finance">WE ALSO OFFFER FINANCE</p>

  <div class="abs notice">
    <p class="notice__small">WE ARE WORKING IN YOUR NEIGHBORHOOD</p>
    <p class="notice__big">YOU CAN FIND US HERE</p>
    <div class="abs address-line"></div>
  </div>
</section>

<section class="card card--back">
  <div class="abs job-photo job-photo--shingles" role="img" aria-label="Crew member nailing new roof shingles"></div>
  <div class="abs job-photo job-photo--gutter" role="img" aria-label="Worker cleaning a gutter"></div>
  <div class="abs job-photo job-photo--painter" role="img" aria-label="Painter spraying house siding"></div>
  <div class="abs job-photo job-photo--siding" role="img" aria-label="Close-up of green shingle siding"></div>
  <div class="abs job-photo job-photo--washing" role="img" aria-label="Worker pressure washing a driveway"></div>
  <div class="abs job-photo job-photo--underlay" role="img" aria-label="Roof deck covered with blue underlayment"></div>
  <div class="abs fleet-photo" role="img" aria-label="Wrapped company pickup truck with ladder rack"></div>

  <div class="abs services">
    <h2 class="services__title">WE ALSO DO</h2>
    <ul class="services__list">
      <li class="services__item"><svg class="services__icon" viewBox="0 0 14 14" aria-hidden="true"><g fill="#fff"><rect width="6" height="6"/><rect x="8" width="6" height="6"/><rect y="8" width="6" height="6"/><rect x="8" y="8" width="6" height="6"/></g></svg>ROOFING</li>
      <li class="services__item"><svg class="services__icon" viewBox="0 0 14 14" aria-hidden="true"><g fill="#fff"><rect width="6" height="6"/><rect x="8" width="6" height="6"/><rect y="8" width="6" height="6"/><rect x="8" y="8" width="6" height="6"/></g></svg>SIDING</li>
      <li class="services__item"><svg class="services__icon" viewBox="0 0 14 14" aria-hidden="true"><g fill="#fff"><rect width="6" height="6"/><rect x="8" width="6" height="6"/><rect y="8" width="6" height="6"/><rect x="8" y="8" width="6" height="6"/></g></svg>GUTTERS</li>
      <li class="services__item"><svg class="services__icon" viewBox="0 0 14 14" aria-hidden="true"><g fill="#fff"><rect width="6" height="6"/><rect x="8" width="6" height="6"/><rect y="8" width="6" height="6"/><rect x="8" y="8" width="6" height="6"/></g></svg>PRESSURE WASHING</li>
      <li class="services__item"><svg class="services__icon" viewBox="0 0 14 14" aria-hidden="true"><g fill="#fff"><rect width="6" height="6"/><rect x="8" width="6" height="6"/><rect y="8" width="6" height="6"/><rect x="8" y="8" width="6" height="6"/></g></svg>PAINTING</li>
      <li class="services__item"><svg class="services__icon" viewBox="0 0 14 14" aria-hidden="true"><g fill="#fff"><rect width="6" height="6"/><rect x="8" width="6" height="6"/><rect y="8" width="6" height="6"/><rect x="8" y="8" width="6" height="6"/></g></svg>ATTIC VENTILATION</li>
    </ul>
  </div>

  <div class="abs sign-off">
    <div class="sign-off__name"><span class="sign-off__mark"></span>Quillby Housecrafters</div>
    <div class="sign-off__rule"></div>
    <div class="sign-off__url">QUILLBYHOUSECRAFTERS.COM</div>
  </div>
</section>

</body>
</html>
```